Amber Hollow Productions

I need a business card design for a new freelance film production company using or incorporating the logo:
I want the card to be creative, minimal, yet professional. Feel free to use a variety of different shapes and sizes/ textures for the card.

Industry/Entity Type

Film Production

```html
<!DOCTYPE html>
<html lang="en">
<head>
<meta charset="utf-8">
<title>Amber Hollow Productions – Business Card</title>
<link rel="stylesheet" href="https://fonts.googleapis.com/css2?family=Josefin+Sans:wght@300&family=Archivo+Black&family=Open+Sans:wght@700&family=Rubik+Dirt&display=swap">
<style>
  :root {
    --brand-blue: #1f3fe0;
    --soft-blue: #b9c6f3;
    --pale-blue: #e6ecfb;
    --ink-grey: #7a7a7a;
    --dark-grey: #444;
    --paper: #ffffff;
  }
  * { margin: 0; padding: 0; box-sizing: border-box; }
  html, body { width: 1200px; height: 1000px; overflow: hidden; background: var(--paper); }
  .canvas { position: relative; width: 1200px; height: 1000px; }
  .card {
    position: absolute; left: 78px; top: 158px; width: 1038px; height: 684px;
    background: var(--paper);
    box-shadow: 0 6px 22px rgba(0,0,0,0.35);
    overflow: hidden;
  }
  .film-art { position: absolute; left: 0; top: 0; width: 1038px; height: 684px; }
  .brand {
    position: absolute; left: 0; width: 100%; text-align: center;
  }
  .brand-mark {
    position: absolute; left: 469px; top: 100px; width: 100px; height: 100px;
    background: var(--brand-blue);
  }
  .brand-name {
    top: 330px;
    font-family: "Josefin Sans", sans-serif; font-weight: 300;
    color: var(--brand-blue); font-size: 46px; letter-spacing: 2px; line-height: 1.1;
  }
  .brand-name span { display: block; font-size: 24px; letter-spacing: 9px; margin-top: 10px; }
  .phone {
    top: 462px;
    font-family: "Archivo Black", sans-serif; font-size: 40px; color: var(--paper);
    letter-spacing: 1px;
    text-shadow: 1px 1px 0 var(--brand-blue), -1px -1px 0 var(--brand-blue),
                 1px -1px 0 var(--brand-blue), -1px 1px 0 var(--brand-blue),
                 4px 5px 4px rgba(0,0,0,0.5);
  }
  .contact {
    top: 524px;
    font-family: "Open Sans", sans-serif; font-weight: 700; color: var(--brand-blue);
  }
  .contact .email { font-size: 19px; letter-spacing: 0.5px; display: block; }
  .contact .web { font-size: 22px; letter-spacing: 0.5px; display: block; margin-top: 4px; }
  .contact .muted { color: var(--ink-grey); }
  .address-band {
    position: absolute; left: 129px; top: 599px; width: 793px; height: 56px;
    background: var(--brand-blue);
    display: flex; align-items: center; justify-content: center;
    font-family: "Rubik Dirt", sans-serif; font-size: 38px; color: var(--paper);
    letter-spacing: 3px; word-spacing: 16px;
  }
</style>
</head>
<body>
<div class="canvas">
  <div class="card">
    <svg class="film-art" viewBox="0 0 1038 684" xmlns="http://www.w3.org/2000/svg">
      <defs>
        <linearGradient id="strip-fade" x1="0" y1="0" x2="0" y2="1">
          <stop offset="0" stop-color="#c9d3f6"/>
          <stop offset="1" stop-color="#eef2fc"/>
        </linearGradient>
        <linearGradient id="curl-top" x1="0" y1="0" x2="0" y2="1">
          <stop offset="0" stop-color="#e6ecfb"/>
          <stop offset="1" stop-color="#5a74e8"/>
        </linearGradient>
        <linearGradient id="curl-bottom" x1="0" y1="0" x2="0" y2="1">
          <stop offset="0" stop-color="#3a58e6"/>
          <stop offset="1" stop-color="#c7d1f6"/>
        </linearGradient>
      </defs>
      <rect role="img" aria-label="Film strip running across the top" x="0" y="40" width="1038" height="78" fill="url(#strip-fade)"/>
      <path role="img" aria-label="Curling film strip, top left" d="M0 80 L120 80 C95 160 60 260 0 340 Z" fill="url(#curl-top)"/>
      <path role="img" aria-label="Curling film strip, top right" d="M1038 80 L920 80 C945 160 980 260 1038 340 Z" fill="url(#curl-top)"/>
      <path role="img" aria-label="Curling film strip, bottom left" d="M0 440 C70 420 120 560 148 684 L0 684 Z" fill="url(#curl-bottom)"/>
      <path role="img" aria-label="Curling film strip, bottom right" d="M1038 420 C960 420 920 560 906 684 L1038 684 Z" fill="url(#curl-bottom)"/>
    </svg>

    <div class="brand-mark" aria-hidden="true"></div>
    <h1 class="brand brand-name">AMBER HOLLOW<span>PRODUCTIONS</span></h1>
    <p class="brand phone">07700 900 123</p>
    <p class="brand contact">
      <span class="email">info@amberhollow<span class="muted">productions</span>.com</span>
      <span class="web">amberhollow<span class="muted">productions</span>.com</span>
    </p>
    <div class="address-band">ADDRESS ADDRESS ADDRESS</div>
  </div>
</div>
</body>
</html>
```